El Molinete Postcard

Please refer to our site for inspiration - I know this is alot of info but ?

El Molinete Reception Hall
4187C Quillmont Rd, Benicia, CA 707-555-0142
www.El-Molinete.example

Located in Benicia, California, we are a new venue that can host a variety of events. We can provide an exceptional space for your next party, reception, quinceañera, birthday party, or meeting! We treat each client with respect and go out of our way to accommodate all of your needs and make your event a success. Conveniently located just off the 680/780 junction, El Molinete is located in a safe, well-lit area with a large private parking area.

The space comes prepared with everything you need to get your party started – chairs and tables with tablecloths, a well-equipped kitchen, and incredible decorations to set the perfect backdrop to your event! Rent just the Lounge for a more intimate get-together, or add the Main Hall for your large sit-down event.

Lounge – Beautiful 1,600 ft2 entry room featuring large living room with conversation sofa seating for 40+ Sound system  Pass-through bar with seating  Fully-equipped 200 ft2 kitchen with
4-burner gas stove, oven, large double sink, full-size refrigerator, 2 microwaves, and ice machine, plus lots of storage and counter space  Newly-remodeled Men’s and Women’s bathrooms

Main Hall – Spacious 24’x80’ room with seating for up to 160 people  2,000 ft2  72” round tables with chairs, each seating up to 8 guests  DJ stand and Sound system  Atmospheric lighting
_______________________________________
Pricing -
Daytime Parties
Available 8AM-2PM
4-hour minimum

Lounge and Kitchen Only
Fri - Sat - Sun : $80/hr
Mon - Thurs : $60/hr

All Areas: Lounge, Kitchen, Main Hall, and Backyard
Fri - Sat - Sun : $120/hr
Mon - Thurs : $100/hr
___________________________________________
Evening Events
Available 3PM-12AM
5-hour minimum

Lounge and Kitchen Only -
Fri - Sat - Sun : $100/hr
Mon - Thurs : $50/hr

Fri - Sat - Sun : $160/hr
Mon - Thurs : $75/hr
___________________________________________________
Looking for a different time frame, all-day rental, or other special request? Let us know!
We'd be happy to provide you with a custom quote for your event.

I am not going to mail this postcard - only a hand out I need info and pricing on back

This is a hand out - will not be mailed

Only need my text on back

• Text and pricing on back
• Vintage feel to it

```html
<!DOCTYPE html>
<html lang="en">
<head>
<meta charset="utf-8">
<title>El Molinete Postcard</title>
<link href="https://fonts.googleapis.com/css2?family=Dancing+Script:wght@400;500&display=swap" rel="stylesheet">
<style>
  :root {
    --beam: #5e5248;
    --wall: #cfc5b8;
    --window: #f4f2ee;
    --sofa: #6f6252;
    --sofa-light: #9d8f7e;
    --floor: #d8cdbf;
    --ink: #3d3a38;
    --title-ink: #2f2c2a;
  }
  html, body {
    margin: 0;
    padding: 0;
    overflow: hidden;
  }
  .postcard {
    position: relative;
    width: 1200px;
    height: 928px;
    overflow: hidden;
    background: #fff;
    font-family: "Dancing Script", cursive;
    color: var(--ink);
  }
  .lounge-photo {
    position: absolute;
    inset: 0;
    background:
      radial-gradient(ellipse 230px 170px at 380px 345px, var(--window) 0%, rgba(244,242,238,0.85) 55%, rgba(244,242,238,0) 100%),
      radial-gradient(ellipse 420px 130px at 300px 600px, rgba(111,98,82,0.9) 0%, rgba(111,98,82,0.55) 60%, rgba(111,98,82,0) 100%),
      radial-gradient(ellipse 220px 120px at 600px 640px, rgba(157,143,126,0.8) 0%, rgba(157,143,126,0) 100%),
      linear-gradient(180deg,
        var(--beam) 0%,
        #8c7f72 7%,
        var(--wall) 16%,
        var(--wall) 50%,
        var(--sofa-light) 60%,
        var(--sofa) 70%,
        var(--sofa-light) 78%,
        var(--floor) 86%,
        #e6ded3 100%);
  }
  .text-veil {
    position: absolute;
    inset: 0;
    background: linear-gradient(90deg,
      rgba(255,255,255,0.3) 0%,
      rgba(255,255,255,0.4) 42%,
      rgba(255,255,255,0.88) 57%,
      rgba(255,255,255,0.92) 100%);
  }
  .copy {
    position: absolute;
    left: 676px;
    top: 48px;
    width: 476px;
  }
  .venue-name {
    margin: 0 0 45px 6px;
    font-size: 76px;
    font-weight: 500;
    line-height: 84px;
    color: var(--title-ink);
  }
  .copy p {
    margin: 0;
    font-size: 25px;
    line-height: 22.6px;
    font-weight: 400;
    letter-spacing: 0.2px;
  }
  .copy p + p {
    margin-top: 24px;
  }
  .copy p.features {
    margin-top: 45px;
  }
  .sep {
    padding: 0 4px;
  }
</style>
</head>
<body>
  <main class="postcard">
    <div class="lounge-photo" role="img" aria-label="Photo of the venue lounge: sofas, armchairs and a glass coffee table beneath a large bright window"></div>
    <div class="text-veil"></div>
    <section class="copy">
      <h1 class="venue-name">El Molinete</h1>
      <p>Located in Benicia, California, we are a new venue that can host a variety of events. We can provide an exceptional space for your next party, reception, quinceañera, birthday party, or meeting! We treat each client with respect and go out of our way to accommodate all of your needs and make your event a success. Conveniently located just off the 680/780 junction, El Molinete is located in a safe, well-lit area with a large private parking area.</p>
      <p>The space comes prepared with everything you need to get your party started – chairs and tables with tablecloths, a well-equipped kitchen, and incredible decorations to set the perfect backdrop to your event! Rent just the Lounge for a more intimate get-together, or add the Main Hall for your large sit-down event.</p>
      <p class="features">Lounge – Beautiful 1,600 ft2 entry room featuring large living room with conversation sofa seating for 40+<span class="sep">•</span>Sound system<span class="sep">•</span>Pass-through bar with seating<span class="sep">•</span>Fully-equipped 200 ft2 kitchen with<br>4-burner gas stove, oven, large double sink, full-size refrigerator, 2 microwaves, and ice machine, plus lots of storage and counter space<span class="sep">•</span>Newly-remodeled Men’s and Women’s bathrooms</p>
    </section>
  </main>
</body>
</html>
```